Tallow Home Buyers

We need a website designed for the a house buying company. It can look and feel similar to a real estate agency, but the messaging is different. Attached in the document below you will see what we are looking for. The main thing we are going for is clean, corporate and approachable. The Logo files are also attached. We want to use the logo and branding throughout the site.

```html
<!DOCTYPE html>
<html lang="en">
<head>
<meta charset="utf-8">
<title>Tallow Home Buyers</title>
<link rel="stylesheet" href="https://fonts.googleapis.com/css2?family=Montserrat:wght@500;600;700;800&family=Open+Sans:wght@400;600;700&display=swap">
<style>
:root{
  --green:#6cb33f;
  --green-dark:#5a9a31;
  --blue:#1c4f91;
  --navy:#163a6b;
  --mint:#e4f6f1;
  --ink:#333;
  --muted:#777;
  --footer:#2a2a2a;
  --line:#d9d9d9;
}
*{box-sizing:border-box;margin:0;padding:0}
html,body{width:1200px;height:5357px;overflow:hidden}
body{position:relative;font-family:"Open Sans",Arial,sans-serif;color:var(--ink);background:#fff}
.abs{position:absolute}
h1,h2,h3,h4,.btn,.nav a{font-family:"Montserrat",Arial,sans-serif}
.btn{display:inline-block;background:var(--green);color:#fff;font-weight:700;font-size:15px;padding:0 22px;line-height:42px;text-transform:uppercase;letter-spacing:.5px}
.btn-blue{background:var(--blue)}
.caret{display:block;margin:0 auto 8px;width:26px;height:12px}
.sec-title{font-size:30px;font-weight:800;color:var(--blue);text-transform:uppercase;text-align:center}

/* header */
.topbar{left:910px;top:0;width:290px;height:30px;background:var(--blue);color:#fff;font-size:15px;font-weight:600;display:flex;align-items:center;justify-content:center;gap:8px}
.brand{left:110px;top:22px;display:flex;align-items:center;gap:12px;font-family:"Montserrat",sans-serif;font-weight:800;font-size:30px;color:var(--blue)}
.brand i{width:22px;height:22px;background:var(--green);display:block}
.nav{left:420px;top:84px;display:flex;gap:34px;align-items:center}
.nav a{font-size:13px;font-weight:700;color:var(--navy);text-decoration:none;text-transform:uppercase}

/* hero */
.hero-photo{left:0;top:125px;width:1200px;height:643px;background:linear-gradient(180deg,#9fb3c6 0%,#5d6f86 40%,#3b4a5e 70%,#6a7a70 100%)}
.hero-copy{left:125px;top:628px;color:#fff}
.hero-copy h1{font-size:34px;font-weight:800;line-height:1.1}
.hero-copy p{font-family:"Montserrat",sans-serif;font-size:21px;font-weight:700;margin-top:4px}
.hero-form{left:125px;top:712px;display:flex}
.hero-form .field{width:485px;height:50px;background:#fff;display:flex;align-items:center;gap:10px;padding-left:16px;color:#888;font-size:15px}
.hero-form .btn{line-height:50px;font-size:17px}

/* reasons */
.reasons{left:125px;top:890px;width:480px}
.reasons h2{font-size:30px;font-weight:800;color:var(--blue)}
.underline{width:60px;height:3px;background:var(--green);margin:8px 0 22px}
.reasons h3{font-size:22px;font-weight:800;color:var(--green)}
.reasons .intro{font-size:13px;line-height:1.6;margin:10px 0 12px;color:#555}
.checks{list-style:none}
.checks li{font-size:12.5px;line-height:1.5;margin-bottom:9px;padding-left:24px;position:relative;color:#555}
.checks li::before{content:"";position:absolute;left:0;top:3px;width:13px;height:13px;background:var(--green)}
.checks b{color:var(--blue);font-weight:600}
.reasons-photo{left:660px;top:902px;width:540px;height:392px;background:linear-gradient(160deg,#cfe0ef 0%,#8fa7a0 45%,#5f6d55 100%)}

/* why us */
.why{left:0;top:1464px;width:1200px;height:536px;background:var(--mint)}
.why .sub{font-family:"Montserrat",sans-serif;font-size:20px;font-weight:700;color:var(--green);text-align:center;margin-top:18px}
.why .tag{text-align:center;font-size:17px;color:#444;margin-top:6px}
.why-grid{position:absolute;left:118px;top:265px;display:flex;gap:30px}
.why-col{width:220px}
.why-col h4{font-size:15px;font-weight:700;color:var(--green);text-transform:uppercase;margin:14px 0 8px}
.why-col p{font-size:11.5px;line-height:1.55;color:#555}
.why-col .more{display:block;font-size:12px;font-weight:700;color:var(--blue);margin-top:10px;font-family:"Montserrat",sans-serif}

/* experts */
.experts{left:0;top:2018px;width:1200px;height:267px;background:linear-gradient(90deg,#1c3457 0%,#2c4d78 50%,#4a6489 100%)}
.experts h2{position:absolute;left:0;width:1200px;top:92px;text-align:center;font-size:36px;font-weight:800;color:#fff;text-transform:uppercase;letter-spacing:1px}
.experts h2 span{color:var(--green)}
.experts .btn{position:absolute;left:513px;top:152px}

/* how it works */
.how{left:0;top:2370px;width:1200px}
.steps{position:absolute;left:160px;top:140px;display:grid;grid-template-columns:repeat(5,170px);grid-template-rows:160px 160px;gap:0 10px}
.cell{display:flex;align-items:center;justify-content:center;text-align:center;font-family:"Montserrat",sans-serif;font-weight:700;font-size:17px;color:var(--blue);position:relative}
.cell.g{background:var(--green)}
.cell.b{background:var(--blue)}
.cell.g::after,.cell.b::after{content:"";position:absolute;left:73px;border-left:12px solid transparent;border-right:12px solid transparent}
.cell.g::after{bottom:-12px;border-top:12px solid var(--green)}
.cell.b::after{top:-12px;border-bottom:12px solid var(--blue)}

/* video */
.video{left:0;top:2964px;width:1200px;height:607px;background:linear-gradient(180deg,#8a9199 0%,#6b747c 50%,#9aa096 100%)}
.video .sec-title{color:#fff;position:absolute;top:100px;width:1200px}
.screen{position:absolute;left:340px;top:196px;width:553px;height:330px;background:#1b1b1b;padding:14px}
.screen-img{width:100%;height:100%;background:linear-gradient(180deg,#b7c3cc 0%,#6d7a83 55%,#4d5a4a 100%);display:flex;align-items:center;justify-content:center}
.stand{position:absolute;left:580px;top:526px;width:72px;height:24px;background:#cfcfcf}

/* reviews */
.reviews{left:0;top:3710px;width:1200px}
.reviews .tag{text-align:center;font-family:"Montserrat",sans-serif;font-weight:700;font-size:17px;margin-top:18px;color:#333}
.cards{position:absolute;left:107px;top:160px;display:flex;gap:36px}
.card{width:304px;height:322px;text-align:center;padding:34px 26px 0}
.card.active{border:1px solid var(--line);box-shadow:0 2px 8px rgba(0,0,0,.08)}
.quote{font-family:Georgia,serif;font-size:56px;line-height:40px;color:var(--green);font-weight:700}
.card h4{font-size:15px;font-weight:600;margin:10px 0 10px;color:#333}
.card p{font-size:11.5px;line-height:1.55;color:#666}
.avatar{width:52px;height:52px;border-radius:50%;background:#a9b4a5;margin:18px auto 8px}
.card .name{font-family:"Montserrat",sans-serif;font-weight:700;font-size:14px;color:var(--blue);text-transform:uppercase}
.card.active .name{color:var(--green)}
.arrow{position:absolute;top:310px;font-size:30px;color:#bbb;font-family:"Montserrat",sans-serif}

/* faq + contact */
.faq-bg{left:0;top:4321px;width:636px;height:607px;background:linear-gradient(180deg,#c9cdd0 0%,#aeb3b6 100%)}
.faq{left:125px;top:4440px;width:500px}
.faq h2{font-size:30px;font-weight:800;color:var(--blue)}
.acc{margin-top:36px}
.acc-item{height:38px;background:var(--blue);color:#fff;font-size:14px;display:flex;align-items:center;padding-left:14px;margin-bottom:12px}
.acc-item.open{background:#fff;color:var(--green);font-weight:600;margin-bottom:0}
.acc-body{background:#fff;padding:4px 14px 14px;font-size:11.5px;line-height:1.55;color:#666;margin-bottom:12px}
.faq .btn{margin-top:6px}
.contact{left:690px;top:4435px;width:392px}
.contact h2{font-size:30px;font-weight:800;color:var(--blue)}
.contact .lead{font-size:14px;margin:12px 0 16px;color:#333}
.input{height:36px;border:1px solid var(--line);font-size:12.5px;color:#666;display:flex;align-items:center;padding-left:12px;margin-bottom:14px;justify-content:space-between;padding-right:12px}
.row{display:flex;gap:14px}
.row>*{flex:1}
.contact .btn{line-height:36px;font-size:13px;padding:0 14px}

/* footer */
.footer{left:0;top:4946px;width:1200px;height:375px;background:var(--footer);color:#ddd}
.footer h4{font-size:15px;font-weight:700;color:var(--green);text-transform:uppercase;position:absolute;top:55px}
.flinks{position:absolute;left:118px;top:100px;list-style:none;font-size:13px;line-height:2.05}
.fcontact{position:absolute;left:357px;top:100px;font-size:12.5px;line-height:1.5}
.fcontact div{display:flex;gap:10px;margin-bottom:18px}
.map{position:absolute;left:650px;top:98px;width:243px;height:152px;background:linear-gradient(135deg,#e6ebe4,#cdd6e0)}
.social{position:absolute;left:957px;top:100px;list-style:none;font-size:13px}
.social li{display:flex;align-items:center;gap:10px;margin-bottom:11px}
.social li i{width:22px;height:22px;background:#fff;display:block}
.fbrand{position:absolute;left:960px;top:300px;display:flex;align-items:center;gap:10px;font-family:"Montserrat",sans-serif;font-weight:800;font-size:18px;color:#fff}
.badge{position:absolute;left:906px;top:295px;width:42px;height:52px;background:#e8e8e8}
.copy{left:0;top:5321px;width:1200px;height:36px;background:var(--green);color:#fff;font-size:12px;display:flex;align-items:center;padding-left:118px}
</style>
</head>
<body>

<!-- header -->
<div class="abs topbar">
  <svg width="14" height="14" viewBox="0 0 24 24"><path fill="#fff" d="M6.6 10.8a15.1 15.1 0 0 0 6.6 6.6l2.2-2.2c.3-.3.7-.4 1-.2 1.1.4 2.3.6 3.6.6.6 0 1 .4 1 1V20c0 .6-.4 1-1 1A17 17 0 0 1 3 4c0-.6.4-1 1-1h3.5c.6 0 1 .4 1 1 0 1.3.2 2.5.6 3.6.1.3 0 .7-.2 1z"/></svg>
  (555) 010-4821
</div>
<div class="abs brand"><i></i>Tallow Home Buyers</div>
<nav class="abs nav">
  <svg width="24" height="22" viewBox="0 0 24 22"><path d="M2 11 12 2l10 9" fill="none" stroke="#6cb33f" stroke-width="2.5"/><path d="M5 10v10h14V10" fill="none" stroke="#6cb33f" stroke-width="2.5"/></svg>
  <a>Why Tallow Home Buyers</a><a>How It Works</a><a>Reasons to Sell</a><a>FAQ</a><a>Contact</a>
</nav>

<!-- hero -->
<div class="abs hero-photo" role="img" aria-label="Modern glass house on a hillside at dusk"></div>
<svg class="abs" style="left:0;top:600px" width="1200" height="168" viewBox="0 0 1200 168">
  <polygon points="0,0 880,0 970,168 0,168" fill="#6cb33f" opacity=".92"/>
  <polygon points="1040,168 1200,20 1200,168" fill="#6cb33f"/>
</svg>
<div class="abs hero-copy">
  <h1>WE BUY HOMES FROM PEOPLE IN A TALLOW!</h1>
  <p>GET YOUR CASH OFFER TODAY.</p>
</div>
<div class="abs hero-form">
  <div class="field">
    <svg width="14" height="18" viewBox="0 0 14 18"><path d="M7 0a7 7 0 0 0-7 7c0 5 7 11 7 11s7-6 7-11a7 7 0 0 0-7-7zm0 9.5A2.5 2.5 0 1 1 7 4.5a2.5 2.5 0 0 1 0 5z" fill="#6cb33f"/></svg>
    Enter Your Street Address
  </div>
  <span class="btn btn-blue">Get A Cash Offer</span>
</div>

<!-- reasons -->
<section class="abs reasons">
  <h2>REASONS TO SELL</h2>
  <div class="underline"></div>
  <h3>THINKING OF SELLING?</h3>
  <p class="intro">No matter your situation, we will buy your home. No need to worry about the condition of the house either – we'll make this a stress-free process and get you cash quickly.</p>
  <ul class="checks">
    <li><b>Retirement</b> – </li>
    <li><b>Downsizing or Upsizing</b> – </li>
    <li><b>Divorce</b> – </li>
    <li><b>Inheritance</b> – Have you inherited a home and you don't want to worry about the headache that comes with it? Sell it to the Tallow experts!</li>
    <li><b>Massive Repairs</b> – Is your home too much to manage? No problem, our team is happy to take it off your hands.</li>
    <li><b>Bad Mortgage</b> – Selling your home is a great way to get out of your current mortgage quick.</li>
    <li><b>Probate</b> – </li>
    <li><b>Moving</b> – Sometimes you just want to move and that's okay too! Let us help you get into your dream home.</li>
  </ul>
  <span class="btn" style="margin-top:10px">More Reasons To Sell »</span>
</section>
<div class="abs reasons-photo" role="img" aria-label="Contemporary home with wood siding and large windows"></div>
<div class="abs" style="left:660px;top:1294px;width:540px;height:8px;background:var(--green)"></div>

<!-- why us -->
<section class="abs why">
  <div style="padding-top:95px">
    <svg class="caret" viewBox="0 0 26 12"><path d="M1 11 13 1l12 10" fill="none" stroke="#6cb33f" stroke-width="3"/></svg>
    <h2 class="sec-title">WHY US?</h2>
    <p class="sub">REASONS PEOPLE WORK WITH TALLOW</p>
    <p class="tag">Benefits of working with us over a realtor.</p>
  </div>
  <div class="why-grid">
    <div class="why-col">
      <svg width="36" height="36" viewBox="0 0 36 36"><circle cx="18" cy="18" r="15" fill="none" stroke="#6cb33f" stroke-width="2.5"/><path d="M18 9v10l6 4" fill="none" stroke="#6cb33f" stroke-width="2.5"/></svg>
      <h4>Quick Turnaround</h4>
      <p>We close on your schedule, often within days, so you can move on without waiting months for a buyer.</p>
      <span class="more">READ MORE</span>
    </div>
    <div class="why-col">
      <svg width="36" height="36" viewBox="0 0 36 36"><rect x="6" y="4" width="24" height="28" fill="none" stroke="#6cb33f" stroke-width="2.5"/><path d="M11 12h14M11 18h14M11 24h9" stroke="#6cb33f" stroke-width="2.5"/></svg>
      <h4>Zero Fees</h4>
      <p>No commissions, closing costs or hidden charges. The offer you accept is the amount you receive.</p>
      <span class="more">READ MORE</span>
    </div>
    <div class="why-col">
      <svg width="36" height="36" viewBox="0 0 36 36"><rect x="4" y="8" width="28" height="22" fill="none" stroke="#6cb33f" stroke-width="2.5"/><path d="M11 19l5 5 9-10" fill="none" stroke="#6cb33f" stroke-width="2.5"/></svg>
      <h4>Stress &amp; Hassle Free</h4>
      <p>No showings, repairs or cleaning required. We handle the paperwork and guide you every step.</p>
      <span class="more">READ MORE</span>
    </div>
    <div class="why-col">
      <svg width="36" height="36" viewBox="0 0 36 36"><rect x="3" y="10" width="30" height="18" fill="none" stroke="#6cb33f" stroke-width="2.5"/><circle cx="18" cy="19" r="4.5" fill="none" stroke="#6cb33f" stroke-width="2.5"/></svg>
      <h4>Cold Hard Cash Fast</h4>
      <p>Get a fair cash offer quickly and receive your funds at closing, with no financing delays.</p>
      <span class="more">READ MORE</span>
    </div>
  </div>
</section>

<!-- experts band -->
<section class="abs experts" role="img" aria-label="Row of modern houses under a dusk sky">
  <h2>WE'RE THE EXPERTS YOU TURN TO IN A <span>TALLOW</span></h2>
  <span class="btn">Get Started »</span>
</section>

<!-- how it works -->
<section class="abs how">
  <svg class="caret" viewBox="0 0 26 12"><path d="M1 11 13 1l12 10" fill="none" stroke="#6cb33f" stroke-width="3"/></svg>
  <h2 class="sec-title">HOW IT WORKS</h2>
  <div class="steps">
    <div class="cell g"><svg width="80" height="60" viewBox="0 0 80 60"><rect x="4" y="6" width="72" height="48" fill="none" stroke="#fff" stroke-width="4"/><path d="M4 6l36 28 36-28" fill="none" stroke="#fff" stroke-width="4"/></svg></div>
    <div class="cell">Speak To A<br>Tallow Expert</div>
    <div class="cell g"><svg width="70" height="70" viewBox="0 0 70 70"><rect x="10" y="8" width="50" height="44" fill="none" stroke="#fff" stroke-width="4"/><path d="M22 30l9 9 17-18" fill="none" stroke="#fff" stroke-width="4"/></svg></div>
    <div class="cell">Receive A<br>Cash Offer</div>
    <div class="cell g"><svg width="80" height="60" viewBox="0 0 80 60"><rect x="4" y="10" width="62" height="38" fill="none" stroke="#fff" stroke-width="4" transform="rotate(-12 35 29)"/><rect x="14" y="16" width="62" height="38" fill="#6cb33f" stroke="#fff" stroke-width="4"/><circle cx="45" cy="35" r="8" fill="none" stroke="#fff" stroke-width="4"/></svg></div>
    <div class="cell">Call or<br>Email Us</div>
    <div class="cell b"><svg width="70" height="70" viewBox="0 0 70 70"><circle cx="30" cy="22" r="12" fill="none" stroke="#fff" stroke-width="4"/><path d="M8 62c0-14 10-22 22-22s22 8 22 22" fill="none" stroke="#fff" stroke-width="4"/><path d="M56 40l3 6 6 1-4.5 4 1 6-5.5-3-5.5 3 1-6-4.5-4 6-1z" fill="none" stroke="#fff" stroke-width="2.5"/></svg></div>
    <div class="cell">Schedule A<br>Quick<br>Walk-Through</div>
    <div class="cell b"><svg width="70" height="70" viewBox="0 0 70 70"><circle cx="38" cy="24" r="16" fill="none" stroke="#fff" stroke-width="4"/><path d="M38 14v20M33 19h8a3 3 0 0 1 0 6h-6a3 3 0 0 0 0 6h8" fill="none" stroke="#fff" stroke-width="3"/><path d="M6 60h14l14-6 18 0" fill="none" stroke="#fff" stroke-width="4"/></svg></div>
    <div class="cell">Get Paid</div>
  </div>
</section>

<!-- video -->
<section class="abs video" role="img" aria-label="Blurred modern house exterior">
  <svg class="caret" style="position:absolute;left:587px;top:76px;margin:0" viewBox="0 0 26 12" width="26" height="12"><path d="M1 11 13 1l12 10" fill="none" stroke="#6cb33f" stroke-width="3"/></svg>
  <h2 class="sec-title">OUR VIDEO</h2>
  <div class="screen">
    <div class="screen-img" role="img" aria-label="Video thumbnail of a modern two-storey home">
      <svg width="70" height="70" viewBox="0 0 70 70"><circle cx="35" cy="35" r="32" fill="rgba(0,0,0,.35)" stroke="#fff" stroke-width="3"/><path d="M28 22v26l20-13z" fill="#fff"/></svg>
    </div>
  </div>
  <div class="stand"></div>
</section>

<!-- reviews -->
<section class="abs reviews">
  <svg class="caret" viewBox="0 0 26 12"><path d="M1 11 13 1l12 10" fill="none" stroke="#6cb33f" stroke-width="3"/></svg>
  <h2 class="sec-title">CLIENT REVIEWS</h2>
  <p class="tag">Hear from satisfied sellers.</p>
  <span class="arrow" style="left:78px">‹</span>
  <span class="arrow" style="left:1105px">›</span>
  <div class="cards">
    <div class="card">
      <div class="quote">“</div>
      <h4>Perfect Home For Me</h4>
      <p>The team made selling simple and fast. They answered every question, gave a fair offer and closed exactly when they said they would. I'd recommend them to anyone.</p>
      <div class="avatar" role="img" aria-label="Client portrait"></div>
      <div class="name">Marcus</div>
    </div>
    <div class="card active">
      <div class="quote">“</div>
      <h4>Perfect Home For Me</h4>
      <p>I needed to sell quickly after a move and they took care of everything. No repairs, no showings, and the cash was in my account within two weeks.</p>
      <div class="avatar" role="img" aria-label="Client portrait"></div>
      <div class="name">Elena Brooks</div>
    </div>
    <div class="card">
      <div class="quote">“</div>
      <h4>Perfect Home For Me</h4>
      <p>Honest, friendly and professional from start to finish. The process was clear and stress free, and we got a great price for our older house.</p>
      <div class="avatar" role="img" aria-label="Client portrait"></div>
      <div class="name">Marcus</div>
    </div>
  </div>
</section>

<!-- faq -->
<div class="abs faq-bg" role="img" aria-label="Faded interior of a bright living room"></div>
<section class="abs faq">
  <h2>FAQ</h2>
  <div class="underline" style="margin-bottom:0"></div>
  <div class="acc">
    <div class="acc-item">+ &nbsp;How fast does this work?</div>
    <div class="acc-item open">– &nbsp;What are your fees?</div>
    <div class="acc-body">There are no fees at all. We cover the closing costs, charge no commissions and pay you the full amount of the cash offer you accept on your home.</div>
    <div class="acc-item">+ &nbsp;What if my home is not in good shape?</div>
  </div>
  <span class="btn">View More »</span>
</section>

<!-- contact -->
<section class="abs contact">
  <h2>CONTACT FORM</h2>
  <div class="underline" style="margin-bottom:0"></div>
  <p class="lead">Speak With a Tallow Expert Today.</p>
  <div class="input">Full Name</div>
  <div class="input">Phone</div>
  <div class="input">Email</div>
  <div class="input">Street Address</div>
  <div class="row"><div class="input">City <span>▾</span></div><div class="input">State <span>▾</span></div></div>
  <div class="row"><div class="input">Zip</div><span class="btn" style="flex:0 0 auto">Get A Cash Offer »</span></div>
</section>

<!-- footer -->
<footer class="abs footer">
  <h4 style="left:118px">Quick Links</h4>
  <ul class="flinks"><li>› Home</li><li>› Why Tallow Home Buyers</li><li>› How It Works</li><li>› Reasons To Sell</li><li>› FAQ</li><li>› Contact</li></ul>
  <h4 style="left:357px">Contact Details</h4>
  <div class="fcontact">
    <div><svg width="14" height="18" viewBox="0 0 14 18"><path d="M7 0a7 7 0 0 0-7 7c0 5 7 11 7 11s7-6 7-11a7 7 0 0 0-7-7z" fill="#6cb33f"/></svg><span>Street Name, City Name Lorem<br>Zipcode – 012345</span></div>
    <div><svg width="14" height="14" viewBox="0 0 24 24"><path fill="#6cb33f" d="M6.6 10.8a15.1 15.1 0 0 0 6.6 6.6l2.2-2.2c.3-.3.7-.4 1-.2 1.1.4 2.3.6 3.6.6.6 0 1 .4 1 1V20c0 .6-.4 1-1 1A17 17 0 0 1 3 4c0-.6.4-1 1-1h3.5c.6 0 1 .4 1 1 0 1.3.2 2.5.6 3.6.1.3 0 .7-.2 1z"/></svg><span>Phone<br>(555) 010-4821</span></div>
    <div><svg width="16" height="12" viewBox="0 0 16 12"><rect x="1" y="1" width="14" height="10" fill="none" stroke="#6cb33f" stroke-width="1.5"/><path d="M1 1l7 6 7-6" fill="none" stroke="#6cb33f" stroke-width="1.5"/></svg><span>Email<br>info@tallowhomebuyers.example</span></div>
  </div>
  <h4 style="left:650px">Location Map</h4>
  <div class="map" role="img" aria-label="Street map showing the office location"></div>
  <h4 style="left:957px">Follow Us</h4>
  <ul class="social"><li><i></i>Community</li><li><i></i>Updates</li><li><i></i>Gallery</li><li><i></i>Contact</li></ul>
  <div class="badge"></div>
  <div class="fbrand">Tallow Home Buyers</div>
</footer>
<div class="abs copy">Copyright © 2019 Tallow Home Buyers – All Rights Reserved.</div>

</body>
</html>
```